PuraVeln

Hi, We are looking for a design Label for our Packaged Drinking Water. We want a label in rich color. The current Label is uploaded. We wish for a much brighter color rather than black. Our current label is in black. We have attached other company labels to give you idea. The Solmira bottle image is also uploaded they use sticker for their bottle, front sticker contains name and back sticker's inner portion has graphics and the outer side has information we also open to that.
Industry/Entity Type
Packaged Drinking Water Bottle Brand
Look and feel
Each slider illustrates characteristics of the customer's brand and the style your logo design should communicate.

```html
<!DOCTYPE html>
<html lang="en">
<head>
<meta charset="utf-8">
<title>PuraVeln – Drinking Water Label</title>
<link href="https://fonts.googleapis.com/css2?family=Krona+One&display=swap" rel="stylesheet">
<style>
  :root {
    --paper: #ffffff;
    --deep-teal: #0f4c58;
    --forest: #04403a;
    --band-teal: #0b5b66;
    --aqua: #5bb8b4;
    --mustard: #e3a933;
    --orange: #e08a12;
    --olive: #97a12a;
    --brick: #d2492c;
    --sand: #f0cdb4;
    --brown: #8d5530;
    --mist: #f2f2f2;
  }
  html, body {
    margin: 0;
    width: 1200px;
    height: 1200px;
    overflow: hidden;
    background: var(--paper);
  }
  .label {
    position: absolute;
    left: 0;
    top: 340px;
    width: 1200px;
    height: 520px;
  }
  .tile {
    position: absolute;
  }
  .brand-band {
    position: absolute;
    left: 450px;
    top: 180px;
    width: 300px;
    height: 84px;
    background: var(--band-teal);
    display: flex;
    align-items: center;
    justify-content: center;
  }
  .brand-name {
    font-family: "Krona One", sans-serif;
    font-size: 27px;
    color: var(--paper);
    text-transform: uppercase;
    letter-spacing: 0.5px;
  }
</style>
</head>
<body>
  <section class="label">
    <!-- left panel -->
    <div class="tile" role="img" aria-label="Geometric pattern of triangles and circles in teal, red and grey" style="left:0;top:0;width:112px;height:120px;background:linear-gradient(135deg,var(--aqua),var(--deep-teal));"></div>
    <div class="tile" role="img" aria-label="Tulip in a white circle with small white blossoms on orange" style="left:0;top:120px;width:112px;height:400px;background:linear-gradient(180deg,var(--mustard),var(--orange));"></div>
    <div class="tile" role="img" aria-label="Geometric giraffe illustration on mustard" style="left:112px;top:0;width:164px;height:210px;background:linear-gradient(135deg,var(--sand),var(--mustard) 55%,var(--olive));"></div>
    <div class="tile" role="img" aria-label="Sunflower illustration on dark teal" style="left:276px;top:0;width:111px;height:110px;background:linear-gradient(180deg,var(--deep-teal),var(--olive));"></div>
    <div class="tile" role="img" aria-label="Rising sun with rays" style="left:387px;top:0;width:63px;height:110px;background:linear-gradient(180deg,var(--brick),#b08a2a);"></div>
    <div class="tile" role="img" aria-label="Mountains with a small castle over water" style="left:276px;top:110px;width:174px;height:100px;background:linear-gradient(90deg,var(--aqua),var(--brown));"></div>
    <div class="tile" role="img" aria-label="Rolling waves in aqua and deep teal" style="left:112px;top:210px;width:263px;height:310px;background:linear-gradient(180deg,var(--mist) 10%,var(--aqua) 45%,var(--deep-teal) 80%);"></div>
    <div class="tile" role="img" aria-label="Small house with a fence" style="left:375px;top:210px;width:75px;height:310px;background:linear-gradient(180deg,var(--deep-teal),var(--mustard) 40%);"></div>

    <!-- center panel -->
    <div class="tile" role="img" aria-label="Sunflower and white blossoms on dark green with a white half circle" style="left:450px;top:0;width:190px;height:180px;background:linear-gradient(90deg,var(--mist) 14%,var(--forest) 14%);"></div>
    <div class="tile" role="img" aria-label="Geometric pattern of triangles and circles" style="left:640px;top:0;width:110px;height:180px;background:linear-gradient(135deg,var(--brick),var(--aqua) 50%,var(--olive));"></div>
    <div class="brand-band">
      <span class="brand-name">PuraVeln</span>
    </div>
    <div class="tile" role="img" aria-label="Elephant with raised trunk above wavy water on mustard" style="left:450px;top:264px;width:190px;height:256px;background:linear-gradient(180deg,var(--mustard) 70%,var(--aqua));"></div>
    <div class="tile" role="img" aria-label="Large stylised elephant head in deep teal on white" style="left:640px;top:264px;width:110px;height:256px;background:linear-gradient(90deg,var(--deep-teal) 60%,var(--mist));"></div>

    <!-- right panel -->
    <div class="tile" role="img" aria-label="Red flower, sunflower, white moon and blossoms on dark green" style="left:750px;top:0;width:275px;height:150px;background:var(--forest);"></div>
    <div class="tile" role="img" aria-label="Elephant spraying water beside leaves on mustard" style="left:750px;top:150px;width:275px;height:370px;background:linear-gradient(180deg,var(--mustard) 60%,var(--deep-teal) 60%,var(--deep-teal) 85%,var(--aqua));"></div>
    <div class="tile" role="img" aria-label="Geometric pattern of triangles and circles" style="left:1025px;top:0;width:175px;height:180px;background:linear-gradient(135deg,var(--aqua),var(--olive) 50%,var(--brick));"></div>
    <div class="tile" role="img" aria-label="Stylised elephant face in deep teal on white" style="left:1025px;top:180px;width:175px;height:340px;background:linear-gradient(180deg,var(--deep-teal) 55%,var(--mist) 55%);"></div>
  </section>
</body>
</html>
```